super clean and modern easy to read. Scandinavian type design.

Hi everyone, we need a wall menu for our retail space. We'd like something that goes along with the style of our website and is also editable (in case we change prices later on). The dimensions for the menu will be about 72 inches wide and about 48 inches high and it will be attached to the wall in our business. Please pull menu wording from this link: http://www.lunaskinloft.example/services

Feel free to shorten the descriptions.

The main sections of the menu are:
luna facials
enhancements
add-ons ($15, $20, and $30)
celebrity facials

Please include the picture of the woman on our homepage in the menu. I'll attach an image.

We would like to start with our process to simplify the steps we take.
1.)Complimentary skin analysis
2.) Choose your service
3.) Choose your products (recommendations are given)
4.) Enjoy!
5.) Further your results with take home products

Last little note, we can email you a larger Logo...Pixel Guild would not let us upload the largest file that we have for the logo.

Target Market(s)

young, fun, hip, suburban women and men.

Industry/Entity Type

Retail

Font styles to use
Sans Serif

Requirements
Must have
• Not too much orange. Keep it clean and not too busy.
• the menu should make it super easy for someone to walk into the store and figure out the process.
• the 5 steps should be listed out first
• the 2 basic facials
• the add ons
• the enhancements (by price)
• the celebrity facials
• Advanced peels
• colors should be mainly blue and white (website) some orange used for framing categories or black. I like clean and not too busy. no cheesy.
Nice to have
• see colors on website. see style.
Should not have
• no clip art! no cursive formal writing.

```html
<!DOCTYPE html>
<html lang="en">
<head>
<meta charset="utf-8">
<title>luna skin loft — Wall Menu</title>
<link rel="stylesheet" href="https://fonts.googleapis.com/css2?family=Oswald:wght@500;600&family=Encode+Sans+Condensed:wght@400;500&display=swap">
<style>
  :root {
    --orange: #f7941d;
    --cyan: #00b6cf;
    --white: #ffffff;
    --ink: #1a1a1a;
    --photo-top: #5d6b7e;
    --photo-bottom: #9fd3df;
  }
  html, body {
    margin: 0;
    padding: 0;
    width: 1200px;
    height: 800px;
    overflow: hidden;
    background: var(--white);
  }
  .menu {
    position: relative;
    width: 1200px;
    height: 800px;
    overflow: hidden;
    background: var(--white);
    font-family: "Encode Sans Condensed", "Arial Narrow", sans-serif;
  }
  .backdrop { position: absolute; inset: 0; }
  .abs { position: absolute; }

  .hero-photo {
    left: 118px; top: 62px; width: 150px; height: 200px;
    border-radius: 70px 70px 60px 60px;
    background: linear-gradient(180deg, var(--photo-top), var(--photo-bottom));
  }

  .brand-name {
    right: 32px; top: 52px;
    margin: 0;
    font-family: "Oswald", sans-serif;
    font-weight: 600;
    font-size: 96px;
    line-height: 1;
    letter-spacing: -2px;
    color: var(--cyan);
  }

  .steps {
    list-style: none; margin: 0; padding: 0;
    font-family: "Oswald", sans-serif;
    font-weight: 600;
    font-size: 24px;
    color: var(--orange);
    text-transform: uppercase;
  }
  .steps li { position: absolute; white-space: nowrap; }

  .burst { position: absolute; }
  .burst-label {
    position: absolute; inset: 0;
    display: flex; flex-direction: column; align-items: center; justify-content: center;
    font-family: "Oswald", sans-serif; font-weight: 600;
    color: var(--white); text-transform: uppercase; line-height: 1;
  }
  .burst-enjoy { left: 930px; top: 215px; width: 150px; height: 150px; transform: rotate(12deg); }
  .burst-enjoy .burst-label { font-size: 38px; }
  .burst-price { left: 588px; top: 380px; width: 150px; height: 150px; transform: rotate(-14deg); }
  .burst-price .burst-label { font-size: 34px; }

  .celebrity { left: 34px; top: 356px; }
  .section-title {
    margin: 0;
    font-family: "Oswald", sans-serif;
    font-weight: 600;
    color: var(--orange);
    text-transform: uppercase;
    line-height: 1;
  }
  .celebrity .section-title { font-size: 42px; margin-bottom: 4px; }
  .celebrity-list {
    list-style: none; margin: 0; padding: 0;
    font-family: "Oswald", sans-serif; font-weight: 500;
    font-size: 23px; line-height: 28px;
    color: var(--cyan); text-transform: uppercase;
  }

  .facials-panel {
    left: 812px; top: 380px; width: 388px; height: 165px;
    color: var(--white); text-align: center;
    font-family: "Oswald", sans-serif;
  }
  .facials-panel h2 { margin: 30px 0 10px; font-size: 40px; font-weight: 600; line-height: 1; }
  .facials-panel p { margin: 0; font-size: 21px; font-weight: 500; line-height: 28px; }

  .column { top: 552px; }
  .column .section-title { font-size: 40px; margin: 2px 0 8px; }
  .col-left { left: 18px; width: 345px; }
  .col-mid { left: 392px; width: 420px; }
  .col-right { left: 834px; width: 350px; }
  .items { list-style: none; margin: 0 0 10px; padding: 0; font-size: 13.5px; line-height: 16.5px; }
  .item-name { color: var(--cyan); }
  .item-note { color: var(--ink); }
</style>
</head>
<body>
<main class="menu">
  <svg class="backdrop" width="1200" height="800" viewBox="0 0 1200 800" aria-hidden="true">
    <path d="M0,0 H1200 V6 C820,18 420,70 250,175 C140,245 60,340 0,420 Z" fill="var(--orange)"/>
    <path d="M1200,6 C820,18 420,70 250,175 C170,225 120,270 85,310 C150,255 260,190 380,150 C600,78 900,34 1200,20 Z" fill="var(--cyan)"/>
    <polygon points="790,348 1200,372 1200,392 812,378" fill="var(--cyan)"/>
    <polygon points="812,378 1200,392 1200,545 818,545" fill="var(--orange)"/>
    <line x1="0" y1="548" x2="1200" y2="548" stroke="var(--orange)" stroke-width="3"/>
    <line x1="372" y1="548" x2="372" y2="800" stroke="var(--orange)" stroke-width="3"/>
    <line x1="818" y1="548" x2="818" y2="800" stroke="var(--orange)" stroke-width="3"/>
  </svg>

  <div class="abs hero-photo" role="img" aria-label="Photo of a smiling guest wearing a colourful layered face mask"></div>

  <h1 class="abs brand-name">luna skin loft</h1>

  <ol class="steps">
    <li style="left:253px; top:156px;">Complimentary skin analysis</li>
    <li style="left:253px; top:200px;">Choose your service</li>
    <li style="left:238px; top:243px;">Choose your products (recommendations are given)</li>
    <li style="left:220px; top:287px;">Further your results with take home products</li>
  </ol>

  <div class="burst burst-enjoy">
    <svg width="150" height="150" viewBox="-1 -1 2 2" aria-hidden="true">
      <polygon fill="var(--orange)" points="1,0 .821,.22 .866,.5 .601,.601 .5,.866 .22,.821 0,1 -.22,.821 -.5,.866 -.601,.601 -.866,.5 -.821,.22 -1,0 -.821,-.22 -.866,-.5 -.601,-.601 -.5,-.866 -.22,-.821 0,-1 .22,-.821 .5,-.866 .601,-.601 .866,-.5 .821,-.22"/>
    </svg>
    <div class="burst-label">Enjoy</div>
  </div>

  <section class="abs celebrity">
    <h2 class="section-title">Celebrity Facials</h2>
    <ul class="celebrity-list">
      <li>Oxygen facial (Marisol Vane’s secret to red carpet skin)</li>
      <li>LED therapy facial (Talia Brooks’s fav)</li>
      <li>Lumique non surgical facelift (Renata Cruz)</li>
      <li>Micro + peel</li>
      <li>Advanced peel</li>
    </ul>
  </section>

  <div class="burst burst-price">
    <svg width="150" height="150" viewBox="-1 -1 2 2" aria-hidden="true">
      <polygon fill="var(--orange)" points="1,0 .821,.22 .866,.5 .601,.601 .5,.866 .22,.821 0,1 -.22,.821 -.5,.866 -.601,.601 -.866,.5 -.821,.22 -1,0 -.821,-.22 -.866,-.5 -.601,-.601 -.5,-.866 -.22,-.821 0,-1 .22,-.821 .5,-.866 .601,-.601 .866,-.5 .821,-.22"/>
    </svg>
    <div class="burst-label"><span>50 min</span><span>$130</span></div>
  </div>

  <section class="abs facials-panel">
    <h2>luna facials</h2>
    <p>lunafacial essential 30 min &nbsp;|&nbsp; $49</p>
    <p>lunafacial advanced 45 min &nbsp;|&nbsp; $69</p>
  </section>

  <section class="abs column col-left">
    <h2 class="section-title">Add-ons $15</h2>
    <ul class="items">
      <li><span class="item-name">wax - brow, chin or lip</span> <span class="item-note">(touch up)</span></li>
      <li><span class="item-name">Magnetic mud mask</span> <span class="item-note">(nourish.mineral infusion)</span></li>
      <li><span class="item-name">Peppermint/eucalyptus scalp massage</span><br><span class="item-note">(invigorating.stress reduction)</span></li>
      <li><span class="item-name">Beard Oil Treatment</span> <span class="item-note">(softens and protects)</span></li>
    </ul>
    <h2 class="section-title">Add-ons $20</h2>
    <ul class="items">
      <li><span class="item-name">Me Time - 20 min extra massage</span> <span class="item-note">(relax.enjoy)</span></li>
      <li><span class="item-name">Hand rejuvenation peel or microderm</span> <span class="item-note">(exfoliating, antiaging)</span></li>
    </ul>
  </section>

  <section class="abs column col-mid">
    <h2 class="section-title">Add-ons $30</h2>
    <ul class="items">
      <li><span class="item-name">crystal microdermabrasion for face and neck or declotte - 2 passes</span><br><span class="item-note">(fine lines, smoothing)</span></li>
      <li><span class="item-name">diamond microdermabrasion for face and neck or declotte - 2 passes</span><br><span class="item-note">(fine lines, smoothing)</span></li>
      <li><span class="item-name">led light therapy - 20 min</span> <span class="item-note">(red antiaging) (blue acne)</span></li>
      <li><span class="item-name">Decollete Treatment</span> <span class="item-note">(Peel or Microderm) (antiaging. Fine lines)</span></li>
      <li><span class="item-name">Whole Face Wax</span> <span class="item-note">(except brows)</span></li>
      <li><span class="item-name">hand treatment - peel + microderm</span> <span class="item-note">(double exfoliation for antiaging)</span></li>
      <li><span class="item-name">facial hydration cocktail -1 pass of microderm + 7 advanced serums to fully hydrate your skin</span> <span class="item-note">(glow.renew)</span></li>
      <li><span class="item-name">microcurrent eye, mouth, or chin</span> <span class="item-note">(non surgical face lift)</span></li>
    </ul>
  </section>

  <section class="abs column col-right">
    <h2 class="section-title">Enhancements $10</h2>
    <ul class="items">
      <li><span class="item-name">Vitamin C</span> <span class="item-note">(radiance + fine lines)</span></li>
      <li><span class="item-name">Peptide</span> <span class="item-note">(plump &amp; smooth)</span></li>
      <li><span class="item-name">Hyaluronic acid</span> <span class="item-note">(moisture.anti-aging)</span></li>
      <li><span class="item-name">Retinol</span> <span class="item-note">(fine lines.age spots)</span></li>
      <li><span class="item-name">Dehydrated Eye Treatment</span></li>
      <li><span class="item-name">Cherry Enzyme Peel</span> <span class="item-note">(antioxidant, healthy glow)</span></li>
      <li><span class="item-name">Pumpkin</span> <span class="item-note">(revitalizes, reduce lines)</span></li>
    </ul>
  </section>
</main>
</body>
</html>
```